Most captivating card ever!

Life Coach - Professional Adventurer - Entrepreneur
I need the worlds most amazing business card for my personal brand. This business card will mostly be used to give to prospective clients for life coaching and business coaching.
Be creative, be adventurous. It needs to stand out. Make people say.. I need this guy!
My background is as an entrepreneur and professional adventurer undertaking extreme expeditions. I am now moving into life coaching.
No specific design ideas, so you have full creativity. Show me your best.
Industry/Entity Type
Life Coaching
Contact Information for Business Card
Dan Pellow
itsdanp.com.au
0468215903
Colors
Designer to choose colors to be used in the design.
Look and feel

```html
<!DOCTYPE html>
<html lang="en">
<head>
<meta charset="utf-8">
<title>Dan Pellow – Business Card</title>
<link rel="stylesheet" href="https://fonts.googleapis.com/css2?family=Oswald:wght@500&family=Open+Sans:wght@400&family=Montserrat:wght@400;600&display=swap">
<style>
  :root {
    --backdrop: #2a2a2a;
    --card: #1b1b1b;
    --card-edge: #232323;
    --silver: #d4d4d4;
    --silver-soft: #bdbdbd;
    --rule: #9a9a9a;
  }
  * { margin: 0; padding: 0; box-sizing: border-box; }
  html, body {
    width: 1200px;
    height: 900px;
    overflow: hidden;
    background: var(--backdrop);
  }
  .canvas {
    position: relative;
    width: 1200px;
    height: 900px;
    display: flex;
    flex-direction: column;
    align-items: center;
    justify-content: center;
    gap: 48px;
  }
  .card {
    position: relative;
    width: 630px;
    height: 350px;
    background: linear-gradient(160deg, var(--card-edge) 0%, var(--card) 60%);
    box-shadow: 0 18px 40px rgba(0,0,0,0.55);
  }
  .name {
    font-family: "Oswald", sans-serif;
    font-weight: 500;
    color: var(--silver);
    text-transform: uppercase;
    letter-spacing: 0.5px;
    line-height: 1;
  }
  .card--front {
    display: flex;
    flex-direction: column;
    align-items: center;
    justify-content: center;
  }
  .card--front .name { font-size: 40px; }
  .tagline {
    margin-top: 8px;
    font-family: "Open Sans", sans-serif;
    font-size: 16px;
    color: var(--silver-soft);
    letter-spacing: 0.2px;
  }
  .card--back {
    display: flex;
    align-items: center;
    justify-content: center;
    gap: 30px;
  }
  .card--back .name { font-size: 42px; }
  .divider {
    width: 1.5px;
    height: 60px;
    background: var(--rule);
  }
  .contact {
    font-family: "Montserrat", sans-serif;
    font-size: 17px;
    color: var(--silver);
    line-height: 1.35;
  }
  .contact-label { font-weight: 600; }
</style>
</head>
<body>
  <main class="canvas">
    <section class="card card--front">
      <h1 class="name">Dan Pellow</h1>
      <p class="tagline">Life Coach - Professional Adventurer - Entrepreneur</p>
    </section>
    <section class="card card--back">
      <h2 class="name">Dan Pellow</h2>
      <span class="divider"></span>
      <div class="contact">
        <p><span class="contact-label">Direct:</span> 0468215903</p>
        <p><span class="contact-label">Web:</span> itsdanp.com.au</p>
      </div>
    </section>
  </main>
</body>
</html>
```